Visit Qalimora Card (School That only teach arabic language) (Guaranteed Payment)

Hi, we are a new school That Teach arabic language in Tunisia, we are looking to conceptulize visit cards for our team. The business card will be printed in color and on Both Sides. We want to communiquer: innovation, excellence, professionalism, leadership and trust. Would we need the business card at the end with the details of everyone of our team (3) General and aussi has one for our center in Tunis. La même designed is used througout of course. Waiting for your sugestions! The address is the Sámi for all the visit cards: 47 Rue des Oliviers Zembra Cedar Building, 3rd Floor 1053 Les Berges du Lac 1, Tunisia aussi la même is the website for all www.qalimora.example The 4 visits Card Those names are: Karim Ouertani Jonas Freiberg Rania Gharbi Qalimora For Karim's Ouertani Visit Card Function name: Managing Partner Phone number: 216 94120386 Email: karim.ouertani@qalimora. example For Rania's visit card function name: Marketing Assistant Phone number: 216 97402615 Email: rania.gharbi@qalimora.example For Jonas's visit card: Function name: Managing Partner Phone number: 49 151 08246519 Mail: @ jonas.freiberg qalimora.example You can find our logo in the attachment.

```html
<!DOCTYPE html>
<html lang="fr">
<head>
<meta charset="utf-8">
<title>Qalimora — cartes de visite</title>
<link rel="stylesheet" href="https://fonts.googleapis.com/css2?family=Open+Sans:wght@400;600&display=swap">
<style>
  :root {
    --brand-blue: #0c4b8c;
    --band-grey: #c4c6c9;
    --card-white: #ffffff;
    --ink-dark: #1d1d1f;
    --backdrop: #e3e5e8;
  }
  * { box-sizing: border-box; margin: 0; padding: 0; }
  html, body { width: 1200px; height: 900px; overflow: hidden; }
  body {
    background: var(--backdrop);
    font-family: "Open Sans", Arial, sans-serif;
    position: relative;
  }
  .card {
    position: absolute;
    left: 250px;
    width: 700px;
    height: 400px;
    background: var(--card-white);
    box-shadow: 0 6px 18px rgba(0,0,0,0.18);
    overflow: hidden;
  }
  .card--front { top: 30px; }
  .card--back { top: 470px; }

  .front-brand {
    position: absolute;
    left: 0; right: 0; top: 130px;
    text-align: center;
    color: var(--brand-blue);
    font-size: 78px;
    font-weight: 400;
    letter-spacing: 1px;
  }
  .front-web {
    position: absolute;
    left: 0; right: 0; top: 268px;
    text-align: center;
    color: var(--ink-dark);
    font-size: 15px;
    letter-spacing: 4px;
  }

  .back-brand {
    position: absolute;
    left: 34px; top: 14px;
    color: var(--brand-blue);
    font-size: 50px;
    line-height: 70px;
    font-weight: 400;
    letter-spacing: 1px;
  }
  .back-wave { position: absolute; inset: 0; }
  .address {
    position: absolute;
    left: 30px; top: 222px;
    color: var(--card-white);
    font-size: 16px;
    line-height: 23px;
    font-style: normal;
  }
  .contact {
    position: absolute;
    right: 30px; top: 252px;
    text-align: right;
    color: var(--card-white);
  }
  .contact-name { font-size: 24px; font-weight: 600; line-height: 30px; }
  .contact-role { font-size: 17px; line-height: 23px; margin-bottom: 8px; }
  .contact-line {
    display: flex; justify-content: flex-end; align-items: center;
    gap: 10px; font-size: 16px; line-height: 23px;
  }
  .contact-line svg { width: 15px; height: 15px; flex: none; }
</style>
</head>
<body>

<section class="card card--front">
  <div class="front-brand">qalimora</div>
  <div class="front-web">www.qalimora.example</div>
</section>

<section class="card card--back">
  <svg class="back-wave" viewBox="0 0 700 400" width="700" height="400" aria-hidden="true">
    <path d="M0,92 C180,144 420,192 700,200 L700,212 C420,204 180,158 0,112 Z" fill="var(--band-grey)"/>
    <path d="M0,124 C180,176 420,212 700,220" fill="none" stroke="var(--brand-blue)" stroke-width="4"/>
    <path d="M0,140 C180,192 420,229 700,236 L700,400 L0,400 Z" fill="var(--brand-blue)"/>
  </svg>
  <div class="back-brand">qalimora</div>

  <address class="address">
    47 Rue des Oliviers Zembra<br>
    Immeuble Cèdres, 3ème étage<br>
    1053 Les Berges du Lac 1, Tunisie
  </address>

  <div class="contact">
    <div class="contact-name">Karim Ouertani</div>
    <div class="contact-role">Managing Partner</div>
    <div class="contact-line">+216 94 120 386
      <svg viewBox="0 0 16 16"><path d="M3.5 1.5l2.5 0 1 3.5-1.8 1.3c.9 1.9 2.4 3.4 4.3 4.3l1.3-1.8 3.5 1v2.5c0 .8-.7 1.5-1.5 1.5C7 13.8 2.2 9 2 3 2 2.2 2.7 1.5 3.5 1.5z" fill="#fff"/></svg>
    </div>
    <div class="contact-line">karim.ouertani@qalimora.example
      <svg viewBox="0 0 16 16"><rect x="1" y="3" width="14" height="10" fill="#fff"/><path d="M1 3l7 6 7-6" fill="none" stroke="var(--brand-blue)" stroke-width="1.3"/></svg>
    </div>
    <div class="contact-line">www.qalimora.example
      <svg viewBox="0 0 16 16"><circle cx="8" cy="8" r="7" fill="#fff"/><g fill="none" stroke="var(--brand-blue)" stroke-width="1"><ellipse cx="8" cy="8" rx="3" ry="7"/><path d="M1 8h14M2.5 4.5h11M2.5 11.5h11"/></g></svg>
    </div>
  </div>
</section>

</body>
</html>
```